Entrepreneur Podcast Cover Graphic Design

My wife and I just launched our podcast but we don't like the current cover. We want a new cover designed so it stands out and reflects the professionalism of our podcast. Attached is our current podcast cover design. We'd like to have it read "Rob & Mireya Interview Entrepreneurs on HARD CHOICES" - We'd also like to feature somehow that we have daily tips included.

Target Market(s)

entrepreneurs,business owners,start ups

Industry/Entity Type

Entrepreneur

Font styles to use
Sans Serif

Colors
0355a3
f37122
9bcb3c
fbed22
ec1f27

Requirements
Must have
• Our names listed: Rob & Mireya
Nice to have
• dark, bold colored background with an outline around the edge
Should not have
• no cartoons, no profanity

```html
<!DOCTYPE html>
<html lang="en">
<head>
<meta charset="utf-8">
<title>Hard Choices – Podcast Cover</title>
<link rel="stylesheet" href="https://fonts.googleapis.com/css2?family=Rye&family=Open+Sans:wght@700&display=swap">
<style>
  :root {
    --maroon: #7f0009;
    --navy: #03497d;
    --orange-frame: #ff5500;
    --orange-corner: #f26722;
    --green-corner: #39b24a;
    --yellow: #fff200;
    --lime: #8dc63f;
  }
  html, body {
    margin: 0;
    padding: 0;
    width: 1200px;
    height: 1200px;
    overflow: hidden;
    background: var(--maroon);
  }
  .cover {
    display: block;
    width: 1200px;
    height: 1200px;
  }
  .show-title {
    font-family: "Open Sans", Arial, sans-serif;
    font-weight: 700;
    fill: var(--yellow);
  }
  .hosts {
    font-family: "Rye", Georgia, serif;
    fill: var(--lime);
  }
  .tagline {
    font-family: "Open Sans", Arial, sans-serif;
    font-weight: 700;
    fill: var(--yellow);
  }
</style>
</head>
<body>
<svg class="cover" viewBox="0 0 1500 1500" xmlns="http://www.w3.org/2000/svg" role="img" aria-label="Hard Choices podcast cover: Rob &amp; Mireya interview entrepreneurs">
  <rect class="backdrop" width="1500" height="1500" fill="var(--maroon)"/>
  <polygon class="corner-blue" points="770,0 1500,0 1500,530" fill="var(--navy)"/>
  <polygon class="corner-orange" points="0,795 0,1500 710,1500" fill="var(--orange-corner)"/>
  <polygon class="corner-green" points="900,1500 1500,1500 1500,1185" fill="var(--green-corner)"/>

  <rect class="frame-outer" x="6" y="6" width="1488" height="1488" fill="none" stroke="var(--orange-frame)" stroke-width="12"/>
  <rect class="frame-inner" x="30" y="33" width="1442" height="1432" fill="none" stroke="var(--orange-frame)" stroke-width="5"/>

  <text class="show-title" x="185" y="588" font-size="330" textLength="1170" lengthAdjust="spacingAndGlyphs">HARD</text>
  <text class="show-title" x="190" y="803" font-size="225" textLength="1170" lengthAdjust="spacingAndGlyphs">CHOICES</text>

  <rect class="host-band" x="0" y="1095" width="1375" height="255" fill="var(--navy)"/>
  <text class="hosts" x="215" y="1225" font-size="110" textLength="1025" lengthAdjust="spacingAndGlyphs">ROB &amp; MIREYA</text>
  <text class="tagline" x="168" y="1305" font-size="82" textLength="1104" lengthAdjust="spacingAndGlyphs">INTERVIEW ENTREPRENEURS</text>
</svg>
</body>
</html>
```